Volren Goods Ltd Stationery Design Project

hi we need to design business cards, letter head, complimentary slips, scribble pads, note pads, envelopes for volren goods ltd.

please see business cards details

Kelvin Obutu

P.O Box 41873 -00312 Nairobi - Kenya
Tel: +254-733-218-904
Email: volrengoods@mailvexo.com

company name should appear on all stationery : Volren Goods Ltd

Industry/Entity Type

Business

Requirements
Must have
• kindly stick to colours in the logo

```html
<!DOCTYPE html>
<html lang="en">
<head>
<meta charset="utf-8">
<title>Volren Goods Ltd – Business Card</title>
<link rel="stylesheet" href="https://fonts.googleapis.com/css2?family=Open+Sans:wght@300;400;600&display=swap">
<style>
  :root {
    --backdrop: #e3e5ee;
    --card-white: #ffffff;
    --brand-navy: #2b4189;
    --brand-orange: #f2a23a;
    --sun-light: #fbd75a;
    --sun-deep: #f5a742;
    --text-white: #ffffff;
  }
  * { margin: 0; padding: 0; box-sizing: border-box; }
  html, body {
    width: 1200px; height: 739px; overflow: hidden;
    background: var(--backdrop);
    font-family: "Open Sans", Arial, sans-serif;
  }
  .stage {
    position: relative; width: 1200px; height: 739px;
    display: flex; align-items: center; justify-content: center; gap: 60px;
  }
  .card {
    position: relative; width: 520px; height: 297px;
    box-shadow: 0 6px 18px rgba(40, 50, 80, 0.18);
  }
  /* Back face */
  .card--back {
    background: radial-gradient(circle at 50% 45%, var(--sun-light) 0%, #f8bd4d 28%, var(--sun-deep) 60%);
  }
  .card--back .sun-pattern {
    position: absolute; inset: 0;
  }
  .card--back .website {
    position: absolute; left: 0; right: 0; top: 50%;
    transform: translateY(-50%);
    text-align: center; color: var(--text-white);
    font-size: 13px; font-weight: 400; letter-spacing: 0.3px;
  }
  /* Front face */
  .card--front { background: var(--card-white); }
  .holder {
    position: absolute; left: 40px; top: 92px;
  }
  .holder__name {
    color: var(--brand-navy); font-size: 19px; font-weight: 400;
    letter-spacing: 0.4px; text-transform: uppercase;
  }
  .holder__role {
    color: var(--brand-orange); font-size: 13px; font-weight: 300; margin-top: 1px;
  }
  .contact {
    position: absolute; left: 40px; top: 180px;
    color: var(--brand-navy); font-size: 12.5px; font-weight: 300; line-height: 16px;
  }
  .contact__company {
    color: var(--brand-orange); font-weight: 400; margin-bottom: 2px; padding-left: 0;
  }
  .contact__row { display: flex; align-items: flex-start; gap: 7px; }
  .contact__icon { width: 11px; height: 16px; flex: 0 0 11px; }
  .contact__text { display: block; }
  .brand {
    position: absolute; right: 38px; top: 110px;
    display: flex; align-items: center; gap: 10px;
  }
  .brand__dot {
    width: 26px; height: 26px; border-radius: 50%; background: var(--brand-orange);
  }
  .brand__name {
    color: var(--brand-navy); font-size: 28px; font-weight: 600;
    letter-spacing: 1.5px; line-height: 1.05; text-transform: uppercase;
  }
</style>
</head>
<body>
<main class="stage">
  <section class="card card--back" aria-label="Business card back">
    <svg class="sun-pattern" width="520" height="297" role="img" aria-label="Decorative sun ornament with swirling rays">
      <circle cx="260" cy="135" r="95" fill="none" stroke="#fcd27a" stroke-width="4" opacity="0.7"/>
    </svg>
    <p class="website">www.VolrenGoods.com</p>
  </section>

  <section class="card card--front" aria-label="Business card front">
    <div class="holder">
      <h1 class="holder__name">Kelvin Obutu</h1>
      <p class="holder__role">Director</p>
    </div>

    <div class="contact">
      <p class="contact__company">Volren Goods Ltd.</p>
      <div class="contact__row">
        <svg class="contact__icon" viewBox="0 0 11 16"><rect x="0" y="5" width="11" height="8" rx="1" fill="var(--brand-orange)"/><path d="M0.5 5.5 L5.5 9.5 L10.5 5.5" fill="none" stroke="#fff" stroke-width="1"/></svg>
        <span class="contact__text">P.O Box 41873 -00312<br>Nairobi - Kenya</span>
      </div>
      <div class="contact__row">
        <svg class="contact__icon" viewBox="0 0 11 16"><circle cx="5.5" cy="8.5" r="5.5" fill="var(--brand-orange)"/><path d="M3.6 6 q0.3 3.5 3.8 5" fill="none" stroke="#fff" stroke-width="1.4" stroke-linecap="round"/></svg>
        <span class="contact__text">+254-733-218-904</span>
      </div>
      <div class="contact__row">
        <svg class="contact__icon" viewBox="0 0 11 16"><rect x="0" y="4" width="11" height="9" rx="1.5" fill="var(--brand-orange)"/><path d="M2 7 h7 M2 10 h5" stroke="#fff" stroke-width="1"/></svg>
        <span class="contact__text">volrengoods@mailvexo.com</span>
      </div>
    </div>

    <div class="brand">
      <span class="brand__dot" aria-hidden="true"></span>
      <span class="brand__name">Volren<br>Goods</span>
    </div>
  </section>
</main>
</body>
</html>
```